Fabrication and machining company needing printed material designs.

Heronfield Vessels, Inc. wants to use appealing visuals as well as informative text to tell potential clients about our capabilities in fabrication and machining. We have a new logo to showcase as well as a new website. The use of print media will allow us to leave tangible information with clients, and therefore the design will need to be concise, informative, and visually appealing.

Full Page Flyer (approx. 8.5" x 11"), front and back design. This will be a detailed offering of capabilities and services for our shop.

Half Page Flyer (approx. 5.5" x 8.5"), front and back design. An abbreviated version of the full page flyer, meant to be easily handed out and stored inside a note book.

Bi-fold business card front and back. General offerings of our services. Minimal if any details. Finished size is twice the size of a business card (approx. 4" x 3.5"), once folded in half will be the same size as a standard business card (approx. 2" x 3.5").

Please use www.heronfieldvesselsinc.example for theme ideas. The font used for our logo is ethnocentric, not to be used for all text.

Target Market(s)

Industrial Consumers

Font styles to use
Sans Serif

```html
<!DOCTYPE html>
<html lang="en">
<head>
<meta charset="utf-8">
<title>Heronfield Vessels, Inc. — Services &amp; Capabilities</title>
<link href="https://fonts.googleapis.com/css2?family=Montserrat:wght@400;600;800&display=swap" rel="stylesheet">
<style>
  :root {
    --orange: #f47b20;
    --ink: #2b2b2b;
    --dark: #1c1c1c;
    --paper: #ffffff;
  }
  * { margin: 0; padding: 0; box-sizing: border-box; }
  html, body { width: 847px; height: 1200px; overflow: hidden; background: var(--paper); }
  .flyer {
    position: relative; width: 847px; height: 1200px; overflow: hidden;
    font-family: "Montserrat", Arial, sans-serif; color: var(--ink); background: var(--paper);
  }
  .backdrop { position: absolute; inset: 0; }
  .page-title {
    position: absolute; left: 48px; top: 28px;
    font-size: 40px; font-weight: 800; color: var(--orange); letter-spacing: 0.2px;
  }
  .column { position: absolute; top: 98px; width: 370px; }
  .column--left { left: 48px; }
  .column--right { left: 436px; width: 380px; }
  .service { margin-bottom: 26px; }
  .service h2 {
    font-size: 26px; font-weight: 400; color: var(--orange); margin-bottom: 8px;
  }
  .service ul { list-style: none; }
  .service li {
    position: relative; padding-left: 26px; font-size: 19px; line-height: 1.3;
    margin-bottom: 3px;
  }
  .service li::before {
    content: ""; position: absolute; left: 6px; top: 10px;
    width: 7px; height: 7px; border-radius: 50%; background: var(--ink);
  }
  .products { position: absolute; left: 375px; top: 735px; color: var(--paper); }
  .products h2 { font-size: 40px; font-weight: 800; color: var(--orange); line-height: 1; margin-bottom: 10px; }
  .products ul { list-style: none; }
  .products li {
    position: relative; padding-left: 50px; font-size: 19px; line-height: 1.3; margin-bottom: 4px;
  }
  .products li::before { content: "»"; position: absolute; left: 4px; top: 0; }
  .contact { position: absolute; left: 48px; top: 1108px; color: var(--paper); font-weight: 800; font-size: 19px; line-height: 1.3; }
  .website { position: absolute; right: 48px; top: 1133px; color: var(--paper); font-weight: 800; font-size: 19px; }
</style>
</head>
<body>
<main class="flyer">
  <svg class="backdrop" width="847" height="1200" viewBox="0 0 847 1200" aria-hidden="true">
    <polygon points="330,650 847,505 847,700" fill="var(--orange)"/>
    <polygon points="0,590 847,690 847,1200 0,1200" fill="var(--dark)"/>
  </svg>

  <h1 class="page-title">OUR SERVICES &amp; CAPABILITIES</h1>

  <section class="column column--left">
    <div class="service">
      <h2>Design &amp; Engineering</h2>
      <ul>
        <li>CAD Drawings</li>
        <li>Engineering Services</li>
        <li>3D Modelling</li>
      </ul>
    </div>
    <div class="service">
      <h2>Fabrication</h2>
      <ul>
        <li>Welding of carbon, stainless, and aluminum.</li>
        <li>CNC plasma table with 8' x 20' cut capacity.</li>
        <li>5' plate x 10' wide roll forming capacity.</li>
        <li>Metal braking, shearing, and punching.</li>
        <li>Lathe and mill machining.</li>
      </ul>
    </div>
  </section>

  <section class="column column--right">
    <div class="service">
      <h2>Sand Blasting &amp; Painting</h2>
      <ul>
        <li>Plural component spray equipmentEpoxy, vinyl ester, fiberglass, &amp; rubberized liner systems capabilities.</li>
        <li>Metal prep to SSPC standards.</li>
        <li>Large production volume.</li>
      </ul>
    </div>
    <div class="service">
      <h2>Insulating Systems</h2>
      <ul>
        <li>Spray foam insulation</li>
        <li>Poly urea</li>
        <li>Fiberglass batting</li>
        <li>Metal wrap</li>
      </ul>
    </div>
  </section>

  <section class="products">
    <h2>OUR PRODUCTS</h2>
    <ul>
      <li>Api 12-F, Api 650 Specification<br>Built Tanks</li>
      <li>Fire Tubes/Tank Heaters</li>
      <li>Tank Coils</li>
      <li>Walkways</li>
      <li>Stairs</li>
      <li>Pump Skids</li>
    </ul>
  </section>

  <p class="contact">CALL US NOW<br>(435) 555 - 0148</p>
  <p class="website">www.heronfieldvesselsinc.example</p>
</main>
</body>
</html>
```